Yard Sign Design Needed

Yard sign needed for mowing & landscaping company. Would like to use the top logo with black background which is attached. Would like MOWING to be in large standout letters. The word "landscaping" can be smaller and more artistic or omitted. Will need room for phone number once design is approved. The phone number will need to stand out and look identical/similar to the word 'MOWING"

```html
<!DOCTYPE html>
<html lang="en">
<head>
<meta charset="utf-8">
<title>Brantley Contractors – Mowing Yard Sign</title>
<link href="https://fonts.googleapis.com/css2?family=Montserrat:wght@600;800&display=swap" rel="stylesheet">
<style>
  :root {
    --page: #ffffff;
    --sign-black: #0a0a0a;
    --white: #ffffff;
    --green: #9acd32;
    --green-deep: #6f8f2f;
    --green-pale: #f4f9ea;
    --ink: #050505;
  }
  html, body {
    margin: 0;
    padding: 0;
    width: 1200px;
    height: 720px;
    overflow: hidden;
    background: var(--page);
  }
  .canvas {
    position: relative;
    width: 1200px;
    height: 720px;
    display: flex;
    align-items: center;
    justify-content: center;
  }
  .yard-sign {
    position: relative;
    width: 427px;
    height: 640px;
    background: var(--sign-black);
    overflow: hidden;
    font-family: "Montserrat", sans-serif;
  }
  .sign-shapes {
    position: absolute;
    inset: 0;
    width: 100%;
    height: 100%;
  }
  .brand {
    position: absolute;
    top: 78px;
    left: 0;
    right: 0;
    text-align: center;
    color: var(--green);
    font-weight: 600;
  }
  .brand-square {
    width: 58px;
    height: 58px;
    margin: 0 auto 30px;
    background: var(--green);
  }
  .brand-name {
    display: block;
    font-size: 42px;
    line-height: 1;
    letter-spacing: 1px;
  }
  .brand-line {
    display: block;
    font-size: 22px;
    line-height: 1.15;
    letter-spacing: 1px;
    margin-top: 4px;
  }
  .brand-llc {
    display: block;
    font-size: 11px;
    letter-spacing: 2px;
    margin-top: 2px;
  }
  .service-main {
    position: absolute;
    top: 330px;
    left: 0;
    right: 0;
    margin: 0;
    text-align: center;
    color: var(--white);
    font-weight: 800;
    font-size: 80px;
    line-height: 1;
    letter-spacing: -1px;
  }
  .service-script {
    position: absolute;
    top: 422px;
    left: 60px;
    width: 310px;
    height: 90px;
    border-radius: 45px;
    background: radial-gradient(ellipse at center, rgba(255,255,255,0.55), rgba(255,255,255,0.08) 70%, rgba(255,255,255,0) 100%);
  }
  .phone {
    position: absolute;
    top: 562px;
    left: 0;
    right: 0;
    margin: 0;
    text-align: center;
    color: var(--ink);
    font-weight: 800;
    font-size: 56px;
    line-height: 1;
    letter-spacing: -1px;
  }
</style>
</head>
<body>
<main class="canvas">
  <section class="yard-sign">
    <svg class="sign-shapes" viewBox="0 0 800 1200" preserveAspectRatio="none" aria-hidden="true">
      <defs>
        <linearGradient id="stripeGradient" x1="0" y1="0" x2="1" y2="0">
          <stop offset="0" stop-color="#e4f0c8"/>
          <stop offset="0.45" stop-color="#9acd32"/>
          <stop offset="1" stop-color="#6f8f2f"/>
        </linearGradient>
        <linearGradient id="baseGradient" x1="0" y1="0" x2="1" y2="0">
          <stop offset="0" stop-color="#f4f9ea"/>
          <stop offset="0.45" stop-color="#9acd32"/>
          <stop offset="1" stop-color="#6f8f2f"/>
        </linearGradient>
      </defs>
      <polygon class="chevron-band" fill="#ffffff"
               points="0,456 400,558 800,456 800,513 400,613 0,513"/>
      <polygon class="chevron-stripe" fill="url(#stripeGradient)"
               points="0,474 400,576 800,474 800,494 400,596 0,494"/>
      <polygon class="base-panel" fill="url(#baseGradient)"
               points="0,936 400,1033 800,936 800,1200 0,1200"/>
    </svg>

    <header class="brand">
      <div class="brand-square"></div>
      <span class="brand-name">BRANTLEY</span>
      <span class="brand-line">CONTRACTORS</span>
      <span class="brand-llc">LLC</span>
    </header>

    <h1 class="service-main">MOWING</h1>
    <div class="service-script" role="img" aria-label="Hand-lettered white brush script reading landscaping"></div>
    <p class="phone">98 765 432</p>
  </section>
</main>
</body>
</html>
```